Business card logo

Hello, I would like a business card for my law firm with a logo composed of my initials "CV". The logo is intended to appear on my business card, my letterhead, envelope and documents from my office. My first and last name (Camille Vautrin) and "Lawyer" must appear next to the logo. I would like the logo and the characters to be in golden color on a dark background (example black, navy blue). I would especially like a refined work on the logo which should be composed of the letters J and R.

```html
<!DOCTYPE html>
<html lang="en">
<head>
<meta charset="UTF-8">
<title>Camille Vautrin – Lawyer Business Card</title>
<link rel="stylesheet" href="https://fonts.googleapis.com/css2?family=Cinzel:wght@500;600&family=EB+Garamond:wght@400;500&display=swap">
<style>
  :root {
    --backdrop: #2b2b2c;
    --card: #1c1d1f;
    --card-edge: #141516;
    --gold: #e6bf2c;
    --serif-display: 'Cinzel', serif;
    --serif-text: 'EB Garamond', serif;
  }
  * { box-sizing: border-box; margin: 0; padding: 0; }
  html, body {
    width: 1200px;
    height: 1200px;
    overflow: hidden;
    background: var(--backdrop);
  }
  .canvas {
    position: relative;
    width: 1200px;
    height: 1200px;
  }
  .card {
    position: absolute;
    left: 150px;
    width: 900px;
    height: 514px;
    background: linear-gradient(135deg, #242527 0%, var(--card) 55%, #18191a 100%);
    border: 1px solid var(--card-edge);
    border-radius: 30px;
    box-shadow: 0 18px 40px rgba(0,0,0,0.45);
    color: var(--gold);
  }
  .card--front { top: 50px; }
  .card--back { top: 636px; }

  .monogram {
    font-family: var(--serif-display);
    font-weight: 600;
    color: var(--gold);
    line-height: 1;
  }

  /* Front */
  .front-lockup {
    position: absolute;
    inset: 0;
    display: flex;
    align-items: center;
    justify-content: center;
    gap: 34px;
  }
  .front-lockup .monogram { font-size: 96px; }
  .wordmark { display: flex; flex-direction: column; align-items: stretch; }
  .wordmark__name {
    font-family: var(--serif-display);
    font-weight: 500;
    font-size: 50px;
    letter-spacing: 1px;
    line-height: 1;
  }
  .wordmark__rule {
    display: flex;
    align-items: center;
    gap: 12px;
    margin-top: 6px;
  }
  .wordmark__rule span.line {
    flex: 1;
    height: 2px;
    background: var(--gold);
  }
  .wordmark__title {
    font-family: var(--serif-display);
    font-size: 22px;
    letter-spacing: 3px;
    line-height: 1;
  }

  /* Back */
  .back-layout {
    position: absolute;
    inset: 0;
    display: flex;
    align-items: center;
    padding-left: 150px;
    gap: 56px;
  }
  .back-layout .monogram { font-size: 150px; }
  .divider {
    width: 2px;
    height: 290px;
    background: var(--gold);
  }
  .details { display: flex; flex-direction: column; }
  .details__name {
    font-family: var(--serif-display);
    font-weight: 600;
    font-size: 36px;
    line-height: 1.05;
  }
  .details__title {
    font-family: var(--serif-display);
    font-weight: 600;
    font-size: 26px;
    margin-left: 22px;
    margin-bottom: 14px;
  }
  .details__address, .contact-list {
    font-family: var(--serif-text);
    font-size: 23px;
    line-height: 1.3;
    margin-left: 44px;
  }
  .contact-list { list-style: none; margin-top: 2px; }
  .contact-list li { display: flex; align-items: center; gap: 12px; }
  .contact-list svg { width: 20px; height: 20px; fill: var(--gold); flex: none; }
</style>
</head>
<body>
<main class="canvas">
  <section class="card card--front" aria-label="Business card front">
    <div class="front-lockup">
      <div class="monogram">CV</div>
      <div class="wordmark">
        <div class="wordmark__name">Camille Vautrin</div>
        <div class="wordmark__rule">
          <span class="line"></span>
          <span class="wordmark__title">LAWYER</span>
          <span class="line"></span>
        </div>
      </div>
    </div>
  </section>

  <section class="card card--back" aria-label="Business card back">
    <div class="back-layout">
      <div class="monogram">CV</div>
      <div class="divider"></div>
      <div class="details">
        <div class="details__name">Camille Vautrin</div>
        <div class="details__title">Lawyer</div>
        <p class="details__address">18 Rue des Tanneurs<br>Second Floor, Lyon 69002</p>
        <ul class="contact-list">
          <li>
            <svg viewBox="0 0 24 24" aria-hidden="true"><path d="M6.6 10.8a15.1 15.1 0 0 0 6.6 6.6l2.2-2.2a1 1 0 0 1 1-.25 11.4 11.4 0 0 0 3.6.57 1 1 0 0 1 1 1V20a1 1 0 0 1-1 1A17 17 0 0 1 3 4a1 1 0 0 1 1-1h3.5a1 1 0 0 1 1 1c0 1.25.2 2.450.57 3.6a1 1 0 0 1-.25 1z"/></svg>
            <span>+33 4 72 10 58 36</span>
          </li>
          <li>
            <svg viewBox="0 0 24 24" aria-hidden="true"><path d="M2 5h20v14H2z M4 7v.5l8 5 8-5V7z" fill-rule="evenodd"/></svg>
            <span>contact@cvautrin-law.fr</span>
          </li>
          <li>
            <svg viewBox="0 0 24 24" aria-hidden="true"><path d="M12 2a10 10 0 1 0 0 20 10 10 0 0 0 0-20zm6.9 6h-3a15 15 0 0 0-1.3-3.8A8 8 0 0 1 18.9 8zM12 4c.8 1.2 1.5 2.5 1.9 4h-3.8c.4-1.5 1.1-2.8 1.9-4zM4.3 14a8 8 0 0 1 0-4h3.4a16 16 0 0 0 0 4zm.8 2h3a15 15 0 0 0 1.3 3.8A8 8 0 0 1 5.1 16zm3-8h-3a8 8 0 0 1 4.3-3.8A15 15 0 0 0 8.1 8zM12 20c-.8-1.2-1.5-2.5-1.9-4h3.8c-.4 1.5-1.1 2.8-1.9 4zm2.3-6H9.7a14 14 0 0 1 0-4h4.6a14 14 0 0 1 0 4zm.3 5.8a15 15 0 0 0 1.3-3.8h3a8 8 0 0 1-4.3 3.8zm1.7-5.8a16 16 0 0 0 0-4h3.4a8 8 0 0 1 0 4z"/></svg>
            <span>www.cvautrin-law.fr</span>
          </li>
        </ul>
      </div>
    </div>
  </section>
</main>
</body>
</html>
```